Tallowmoor Letterheads Design

Hello, we have just upgraded this project for a guaranteed payment.

We are currently going through a re-branding exercise internally. Our logo is attached as a PDF file.

We are happy with our logo but would like to investigate how we can best apply the logo to our letterheads and compliment slips.

We are a quality printing company in England. Despite our name we are very professional and offer a personal service.

Our new website is under construction and here is a link to show you how it looks: http://brackenpress.v4ntor.co.uk

The style must be professional and steer away from "tacky" otherwise it makes our company look very low budget and just a bit silly.

We would like to see elements of creativity though, so please, nothing too boring.

I have attached our new logo, there is an option for use on white or black.

Cheers
Tallowmoor Team

Reason: We have increased the deadline due to an internal delay to things, we now have more time before we need anything to be printed.

Industry/Entity Type

Construction

Requirements
Must have
• IMPORTANT! Please do not tweak or change our logo in any way. A few designs show vast changes in the logo, this is not what we require. Please do not change the logo in any way. Thanks
Nice to have
• Classy but approachable. Elements of "quirky" would be nice to see.
Should not have
• A Tacky feel

```html
<!DOCTYPE html>
<html lang="en">
<head>
<meta charset="utf-8">
<title>Tallowmoor Stationery</title>
<link href="https://fonts.googleapis.com/css2?family=Barlow:wght@500;700&family=Kalam:wght@400&display=swap" rel="stylesheet">
<style>
  :root {
    --backdrop: #ececec;
    --paper: #ffffff;
    --ink: #1f1f1f;
    --brand-pink: #e0306f;
    --mark-tint: #f6d3df;
    --mark-grey: #e4e4e4;
  }
  html, body {
    margin: 0;
    width: 1200px;
    height: 800px;
    overflow: hidden;
    background: var(--backdrop);
    font-family: "Barlow", "Helvetica Neue", Arial, sans-serif;
    color: var(--ink);
  }
  .canvas { position: relative; width: 1200px; height: 800px; }

  .sheet {
    position: absolute;
    background: var(--paper);
    overflow: hidden;
  }
  .letterhead { left: 202px; top: 130px; width: 382px; height: 540px; }
  .compliment-slip { left: 616px; top: 306px; width: 382px; height: 180px; }

  .band { position: absolute; height: 11px; }
  .band--ink { background: var(--ink); }
  .band--pink { background: var(--brand-pink); }

  .brand {
    position: absolute;
    display: flex;
    align-items: center;
    gap: 5px;
    font-weight: 700;
    color: var(--ink);
    white-space: nowrap;
  }
  .brand__dot { border-radius: 50%; background: var(--brand-pink); flex: none; }
  .letterhead .brand { left: 16px; top: 40px; font-size: 17px; }
  .letterhead .brand__dot { width: 14px; height: 14px; }
  .compliment-slip .brand { left: 16px; top: 30px; font-size: 12px; }
  .compliment-slip .brand__dot { width: 10px; height: 10px; }

  .watermark-mark {
    position: absolute;
    background: radial-gradient(ellipse at 40% 55%, var(--mark-tint) 0%, var(--mark-tint) 45%, var(--mark-grey) 62%, rgba(255,255,255,0) 78%);
  }
  .letterhead .watermark-mark { left: -10px; top: 315px; width: 210px; height: 215px; }
  .compliment-slip .watermark-mark { left: -6px; top: 84px; width: 80px; height: 80px; }

  .compliments-title {
    position: absolute;
    right: 16px;
    top: 14px;
    font-family: "Kalam", "Comic Sans MS", cursive;
    font-size: 13px;
    color: var(--brand-pink);
    letter-spacing: 0.3px;
  }

  .contact {
    position: absolute;
    right: 16px;
    text-align: right;
    font-weight: 500;
    font-size: 7.3px;
    line-height: 1.3;
  }
  .letterhead .contact { top: 478px; }
  .compliment-slip .contact { top: 119px; font-size: 6.6px; }
  .contact__row {
    display: flex;
    justify-content: flex-end;
    align-items: center;
    gap: 5px;
    margin-bottom: 3px;
  }
  .contact__row--address { align-items: flex-start; }
  .contact__item { display: inline-flex; align-items: center; gap: 4px; }
  .icon { width: 8px; height: 8px; flex: none; color: var(--brand-pink); }
</style>
</head>
<body>
<div class="canvas">

  <section class="sheet letterhead" aria-label="Letterhead">
    <div class="band band--ink" style="left:0;top:0;width:235px"></div>
    <div class="band band--pink" style="left:240px;top:0;width:142px"></div>

    <div class="brand"><span class="brand__dot"></span>Tallowmoor</div>

    <div class="watermark-mark" role="img" aria-label="Faint oversized brand mark decoration"></div>

    <address class="contact" style="font-style:normal">
      <div class="contact__row contact__row--address">
        <span>18 Market Row, Ashcombe-On-The-Wold,<br>Ashcombe, Devon, EX9 4QT</span>
        <svg class="icon" viewBox="0 0 10 10"><path d="M5 0.5a3.2 3.2 0 0 0-3.2 3.2C1.8 6 5 9.5 5 9.5S8.2 6 8.2 3.7A3.2 3.2 0 0 0 5 0.5zm0 4.4a1.2 1.2 0 1 1 0-2.4 1.2 1.2 0 0 1 0 2.4z" fill="currentColor"/></svg>
      </div>
      <div class="contact__row">
        <span class="contact__item">sales@tallowmoor.co.uk
          <svg class="icon" viewBox="0 0 10 10"><rect x="0.8" y="2" width="8.4" height="6" fill="none" stroke="currentColor" stroke-width="0.9"/><path d="M0.8 2 5 5.6 9.2 2" fill="none" stroke="currentColor" stroke-width="0.9"/></svg>
        </span>
        <span class="contact__item">0207 946 0318
          <svg class="icon" viewBox="0 0 10 10"><path d="M2.3 0.8 3.8 2.6 3 3.8c.6 1.3 1.8 2.5 3.2 3.2L7.4 6.2 9.2 7.7 8.2 9.2C4.4 9 1 5.6 0.8 1.8z" fill="none" stroke="currentColor" stroke-width="0.9"/></svg>
        </span>
      </div>
      <div class="contact__row">
        <span>www.brackenpress.v4ntor.co.uk</span>
        <svg class="icon" viewBox="0 0 10 10"><circle cx="5" cy="5" r="4" fill="none" stroke="currentColor" stroke-width="0.8"/><ellipse cx="5" cy="5" rx="1.8" ry="4" fill="none" stroke="currentColor" stroke-width="0.7"/><path d="M1 5h8" stroke="currentColor" stroke-width="0.7"/></svg>
      </div>
    </address>

    <div class="band band--pink" style="left:0;bottom:0;width:142px"></div>
    <div class="band band--ink" style="left:146px;bottom:0;width:236px"></div>
  </section>

  <section class="sheet compliment-slip" aria-label="Compliment slip">
    <div class="band band--ink" style="left:0;top:0;width:235px"></div>
    <div class="band band--pink" style="left:240px;top:0;width:142px"></div>

    <div class="brand"><span class="brand__dot"></span>Tallowmoor</div>
    <div class="compliments-title">With Compliments</div>

    <div class="watermark-mark" role="img" aria-label="Faint brand mark decoration"></div>

    <address class="contact" style="font-style:normal">
      <div class="contact__row contact__row--address">
        <span>18 Market Row, Ashcombe-On-The-Wold,<br>Ashcombe, Devon, EX9 4QT</span>
        <svg class="icon" viewBox="0 0 10 10"><path d="M5 0.5a3.2 3.2 0 0 0-3.2 3.2C1.8 6 5 9.5 5 9.5S8.2 6 8.2 3.7A3.2 3.2 0 0 0 5 0.5zm0 4.4a1.2 1.2 0 1 1 0-2.4 1.2 1.2 0 0 1 0 2.4z" fill="currentColor"/></svg>
      </div>
      <div class="contact__row">
        <span class="contact__item">sales@tallowmoor.co.uk
          <svg class="icon" viewBox="0 0 10 10"><rect x="0.8" y="2" width="8.4" height="6" fill="none" stroke="currentColor" stroke-width="0.9"/><path d="M0.8 2 5 5.6 9.2 2" fill="none" stroke="currentColor" stroke-width="0.9"/></svg>
        </span>
        <span class="contact__item">0207 946 0318
          <svg class="icon" viewBox="0 0 10 10"><path d="M2.3 0.8 3.8 2.6 3 3.8c.6 1.3 1.8 2.5 3.2 3.2L7.4 6.2 9.2 7.7 8.2 9.2C4.4 9 1 5.6 0.8 1.8z" fill="none" stroke="currentColor" stroke-width="0.9"/></svg>
        </span>
      </div>
      <div class="contact__row">
        <span>www.brackenpress.v4ntor.co.uk</span>
        <svg class="icon" viewBox="0 0 10 10"><circle cx="5" cy="5" r="4" fill="none" stroke="currentColor" stroke-width="0.8"/><ellipse cx="5" cy="5" rx="1.8" ry="4" fill="none" stroke="currentColor" stroke-width="0.7"/><path d="M1 5h8" stroke="currentColor" stroke-width="0.7"/></svg>
      </div>
    </address>

    <div class="band band--pink" style="left:0;bottom:0;width:142px"></div>
    <div class="band band--ink" style="left:146px;bottom:0;width:236px"></div>
  </section>

</div>
</body>
</html>
```